IT Tradingsystem for car dealers needs Business Card Design

We need a fresh and modern design for our new business cards.

We develop a it-business system for car dealers in Sweden, Norway and on our way down to further countries in Europe, hence the namechange to Velmora Systems AB. The site can be found at www.velmora-example.com. The startpage is also in for an update/modernization soon so don't take to much from here.

We are looking to print double sided, 4-colour cards.

We want to look professional, modern and serious. Open to cooler suggestions, but not too crazy. We need to make a good and serious impression on our potential customers. It needs to reflect our scandinavian design values and layout.

Preferably with the full Velmora logo in good size on the back, so the small print on the logo can be read easily.

Text that needs to go on the cards:
-------

Petter Harald Brandt
Founder

Direct +46 70-512 96 47
Support 08-539 27 614
ph.brandt@velmora-example.com

Velmora Systems AB
Box 7918
118 42 Stockholm

Velmora-example.com
Sordimpex.se

--------
Good luck and thanks!

PS. If you need more input or see what our previous cards looked like, don't hesitate to contact me!

Target Market(s)

Decision makers / executives at brand cardealers

Industry/Entity Type

Automotive

Contact Information for Business Card

Normal size

Requirements
Must have
• Full logo
Nice to have
• Base on our orange colors
Should not have
• No fonts with serif, and not too much graphics

```html
<!DOCTYPE html>
<html lang="en">
<head>
<meta charset="utf-8">
<title>Velmora Systems AB – Business Cards</title>
<link rel="stylesheet" href="https://fonts.googleapis.com/css2?family=Open+Sans:wght@400;600;700&display=swap">
<style>
  :root {
    --backdrop: #2b2826;
    --card: #0d0d0d;
    --orange: #f47c20;
    --orange-light: #f6a06a;
    --white: #f2f2f2;
    --grey: #bdbdbd;
  }
  * { margin: 0; padding: 0; box-sizing: border-box; }
  html, body {
    width: 1200px; height: 900px; overflow: hidden;
    background: var(--backdrop);
    font-family: "Open Sans", sans-serif;
  }
  .canvas {
    width: 1200px; height: 900px;
    display: flex; align-items: center; justify-content: center; gap: 40px;
  }
  .card {
    width: 540px; height: 310px;
    background: var(--card);
    position: relative;
    box-shadow: 0 10px 30px rgba(0,0,0,.45);
  }

  /* Contact side */
  .brand-area {
    position: absolute; left: 0; top: 0; width: 250px; height: 100%;
    display: flex; align-items: center; justify-content: center; gap: 12px;
  }
  .brand-square { width: 26px; height: 26px; background: var(--orange); }
  .brand-name { color: var(--orange); font-weight: 700; font-size: 36px; letter-spacing: -.5px; }
  .divider {
    position: absolute; left: 262px; top: 70px; width: 1px; height: 170px;
    background: linear-gradient(to bottom, transparent, var(--orange) 30%, var(--orange) 70%, transparent);
  }
  .contact {
    position: absolute; left: 282px; top: 58px;
    color: var(--white); font-size: 13px; line-height: 1.35;
  }
  .person-name { color: var(--orange); font-weight: 700; font-size: 15px; }
  .person-role { margin-bottom: 12px; }
  .company { font-weight: 700; }
  .address { margin-bottom: 12px; }
  .contact-list { list-style: none; }
  .contact-list li { display: flex; align-items: center; gap: 6px; }
  .contact-list svg { width: 11px; height: 11px; flex: none; }

  /* Logo side */
  .logo-lockup {
    position: absolute; left: 0; top: 0; width: 100%; height: 100%;
    display: flex; align-items: center; justify-content: center; gap: 16px;
  }
  .logo-square { width: 44px; height: 44px; background: var(--orange); }
  .logo-name { color: var(--white); font-weight: 700; font-size: 52px; line-height: 1; letter-spacing: -1px; }
  .logo-tagline { color: var(--grey); font-size: 13px; margin-top: 4px; letter-spacing: .3px; }
</style>
</head>
<body>
<main class="canvas">

  <section class="card card-contact">
    <div class="brand-area">
      <span class="brand-square"></span>
      <span class="brand-name">Velmora</span>
    </div>
    <div class="divider"></div>
    <div class="contact">
      <p class="person-name">Petter Harald Brandt</p>
      <p class="person-role">Founder</p>
      <p class="company">Velmora Systems AB</p>
      <p>Box 7918,</p>
      <p class="address">118 42 Stockholm</p>
      <ul class="contact-list">
        <li>
          <svg viewBox="0 0 12 12"><path fill="var(--orange)" d="M2.5 1l2 2-1 1.5c.7 1.5 1.8 2.6 3.3 3.3L8.3 6.8l2 2-1.3 2C5 10.5 1.5 7 1.2 2.3z"/></svg>
          Direct- +46 70-512 96 47
        </li>
        <li>
          <svg viewBox="0 0 12 12"><circle cx="6" cy="6" r="5.5" fill="var(--orange)"/><path d="M3 6.5a3 3 0 0 1 6 0" stroke="var(--card)" stroke-width="1.2" fill="none"/></svg>
          Support- 08-539 27 614
        </li>
        <li>
          <svg viewBox="0 0 12 12"><rect x="0.5" y="2" width="11" height="8" fill="var(--orange)"/><path d="M.5 2l5.5 4.5L11.5 2" stroke="var(--card)" fill="none"/></svg>
          ph.brandt@velmora-example.com
        </li>
        <li>
          <svg viewBox="0 0 12 12"><circle cx="6" cy="6" r="5.5" fill="var(--orange)"/><path d="M.5 6h11M6 .5c-2.5 3-2.5 8 0 11M6 .5c2.5 3 2.5 8 0 11" stroke="var(--card)" stroke-width=".8" fill="none"/></svg>
          Velmora-example.com
        </li>
        <li>
          <svg viewBox="0 0 12 12"><circle cx="6" cy="6" r="5.5" fill="var(--orange)"/><path d="M.5 6h11M6 .5c-2.5 3-2.5 8 0 11M6 .5c2.5 3 2.5 8 0 11" stroke="var(--card)" stroke-width=".8" fill="none"/></svg>
          Sordimpex.se
        </li>
      </ul>
    </div>
  </section>

  <section class="card card-logo">
    <div class="logo-lockup">
      <span class="logo-square"></span>
      <div>
        <p class="logo-name">Velmora</p>
        <p class="logo-tagline">Autoprov | Remarketing | sordimpex.se</p>
      </div>
    </div>
  </section>

</main>
</body>
</html>
```